Locksmiths Business Card Designs needed!!

I need a business card design for my new small locksmith business.
I would love my business card to be simple, (not too many photos of locks or keys) but strong images so that everyone can recognise it is locksmithing business without reading the words.

I want all information i put in upper article to appear on front side in anyway depending on your design of suggestions and on the back side I would love to mention theses;
-24 /7 mobile services (including weekends & public holidays)
-Residential / Commercial/ Automotive
-Opening / Repair / Installation
-Cut keys

Im not a native english speaker so you can fix the words or expressions as you think it is right and natural.

I realised that in the business names, there is too many "locks" and "s" so I would love to seperate the words somehow so that it is more natural when someone read the business name on the card. for example,put the part of "Bright Harbor Access" first line and the part of "Locksmiths" on the other line....I am just suggesting..doesn't need to be like that..but it should say "Locksmiths" as it is locksmiths business. :)

Target Market(s)

all generations

Industry/Entity Type

Locksmith

Contact Information for Business Card

business name : Bright Harbor Access Services
ABN 41862093715
Name : Dean Rowe (푸른 문지기)
phone : 0468 219 357
email : brightharboraccess@mailverte.net

Requirements
Must have
• A symbol of either a key or a lock
Nice to have
• I like the symbol of a key in the photo I have attached here. So maybe, if you couldn't find any other good symbols I am happy to have the symbol on the business somehow.
Should not have
• Too many keys or locks

```html
<!DOCTYPE html>
<html lang="en">
<head>
<meta charset="utf-8">
<title>Bright Harbor Access Locksmiths – Business Cards</title>
<link rel="stylesheet" href="https://fonts.googleapis.com/css2?family=Alegreya:ital,wght@0,400;0,500;0,700;1,400;1,700&display=swap">
<style>
  :root {
    --page-bg: #e9e6e1;
    --card-bg: #2b2b2b;
    --card-edge: #1f1f1f;
    --text-light: #f4f4f2;
    --accent-orange: #e8691e;
    --accent-green: #6aa43a;
  }
  * { margin: 0; padding: 0; box-sizing: border-box; }
  html, body {
    width: 1200px; height: 900px; overflow: hidden;
    background: var(--page-bg);
    font-family: "Alegreya", Georgia, serif;
    color: var(--text-light);
  }
  .canvas { position: relative; width: 1200px; height: 900px; }
  .icon-defs { position: absolute; width: 0; height: 0; }
  .card {
    position: absolute;
    width: 560px; height: 340px;
    background: var(--card-bg);
    border: 1px solid var(--card-edge);
    box-shadow: 0 10px 28px rgba(0,0,0,0.28);
  }
  .card--front { left: 30px; top: 130px; }
  .card--back { left: 610px; top: 430px; }

  .key-bullet {
    width: 26px; height: 12px;
    margin-right: 10px; vertical-align: middle;
    fill: var(--accent-green);
  }
  .key-bullet--large { width: 30px; height: 14px; }

  /* Front */
  .front__name {
    position: absolute; top: 24px; left: 0; right: 0;
    text-align: center; font-weight: 700; font-size: 32px;
  }
  .front__company {
    position: absolute; top: 76px; left: 30px; width: 380px;
    text-align: center; font-weight: 500; font-size: 25px; line-height: 1.1;
  }
  .front__abn {
    position: absolute; top: 110px; left: 30px; width: 380px;
    text-align: center; font-size: 18px;
  }
  .front__mark {
    position: absolute; top: 100px; right: 30px; width: 120px;
    display: flex; flex-direction: column; align-items: center; gap: 8px;
    text-align: center;
  }
  .brand-square { width: 28px; height: 28px; background: var(--accent-orange); }
  .brand-name { color: var(--accent-orange); font-weight: 700; font-size: 19px; line-height: 1.1; }
  .front__contacts {
    position: absolute; left: 30px; top: 200px;
    list-style: none; font-style: italic; font-weight: 700; font-size: 19px;
  }
  .front__contacts li { margin-bottom: 34px; white-space: nowrap; }

  /* Back */
  .back__company {
    position: absolute; top: 22px; left: 0; right: 0;
    text-align: center; font-weight: 500; font-size: 26px;
  }
  .back__tagline {
    position: absolute; top: 60px; left: 0; right: 0;
    text-align: center; font-style: italic; font-weight: 700; font-size: 17px; line-height: 1.2;
  }
  .back__mark {
    position: absolute; top: 140px; left: 215px; width: 130px;
    display: flex; flex-direction: column; align-items: center; gap: 8px;
    text-align: center;
  }
  .back__cut-keys {
    position: absolute; top: 262px; left: 215px; width: 130px;
    text-align: center; color: var(--accent-orange);
    font-style: italic; font-weight: 700; font-size: 20px;
  }
  .back__sectors {
    position: absolute; left: 26px; top: 178px; list-style: none; font-size: 24px;
  }
  .back__sectors li { margin-bottom: 8px; }
  .back__services {
    position: absolute; left: 375px; top: 130px; list-style: none;
    font-style: italic; font-weight: 700; font-size: 19px;
  }
  .back__services li { margin-bottom: 10px; }
</style>
</head>
<body>
<main class="canvas">
  <svg class="icon-defs" aria-hidden="true">
    <defs>
      <symbol id="icon-key" viewBox="0 0 26 12">
        <circle cx="5" cy="6" r="5"/>
        <rect x="9" y="4.5" width="17" height="3"/>
        <rect x="18" y="7" width="2.5" height="4"/>
        <rect x="22.5" y="7" width="2.5" height="3"/>
      </symbol>
    </defs>
  </svg>

  <section class="card card--front" aria-label="Business card front">
    <h1 class="front__name">Dean Rowe</h1>
    <p class="front__company">Bright Harbor Access Locksmiths</p>
    <p class="front__abn">ABN 41862093715</p>
    <div class="front__mark">
      <span class="brand-square" aria-hidden="true"></span>
      <span class="brand-name">Bright Harbor<br>Access</span>
    </div>
    <ul class="front__contacts">
      <li><svg class="key-bullet" aria-hidden="true"><use href="#icon-key"/></svg>phone : 0468 219 357</li>
      <li><svg class="key-bullet" aria-hidden="true"><use href="#icon-key"/></svg>email : brightharboraccess@mailverte.net</li>
    </ul>
  </section>

  <section class="card card--back" aria-label="Business card back">
    <h2 class="back__company">Bright Harbor Access Locksmiths</h2>
    <p class="back__tagline">24 /7 mobile services &nbsp; All suburbs<br>including weekends &amp; public holidays</p>
    <ul class="back__sectors">
      <li><svg class="key-bullet key-bullet--large" aria-hidden="true"><use href="#icon-key"/></svg>Residential</li>
      <li><svg class="key-bullet key-bullet--large" aria-hidden="true"><use href="#icon-key"/></svg>Commercial</li>
      <li><svg class="key-bullet key-bullet--large" aria-hidden="true"><use href="#icon-key"/></svg>Automotive</li>
    </ul>
    <div class="back__mark">
      <span class="brand-square" aria-hidden="true"></span>
      <span class="brand-name">Bright Harbor<br>Access</span>
    </div>
    <p class="back__cut-keys">Cut keys</p>
    <ul class="back__services">
      <li><svg class="key-bullet" aria-hidden="true"><use href="#icon-key"/></svg>Opening</li>
      <li><svg class="key-bullet" aria-hidden="true"><use href="#icon-key"/></svg>Repair</li>
      <li><svg class="key-bullet" aria-hidden="true"><use href="#icon-key"/></svg>Installation</li>
    </ul>
  </section>
</main>
</body>
</html>
```